Derek Folsom Resume

Need to update resume with latest position and ensure it stays to 2 pages, may need advice on what to get rid of and simply clean it up, already have a format that i like but am open to change but don't want to spend a fortune

```html
<!DOCTYPE html>
<html lang="en">
<head>
<meta charset="utf-8">
<title>Derek Folsom – Resume Page 3</title>
<link href="https://fonts.googleapis.com/css2?family=Libre+Baskerville:wght@700&family=PT+Sans:wght@400;700&display=swap" rel="stylesheet">
<style>
  :root {
    --navy: #132a5e;
    --ink: #111111;
    --band: #ebebeb;
    --frame: #555555;
    --paper: #ffffff;
  }
  * { box-sizing: border-box; margin: 0; padding: 0; }
  html, body { width: 946px; height: 1200px; overflow: hidden; background: var(--paper); }
  body {
    position: relative;
    font-family: "PT Sans", sans-serif;
    font-size: 14px;
    color: var(--ink);
  }
  .page-header {
    position: absolute; top: 32px; left: 24px; right: 86px;
    display: flex; justify-content: space-between;
    font-family: "Libre Baskerville", serif;
    font-weight: 700; font-variant: small-caps;
    font-size: 19px; letter-spacing: 1.5px;
    color: var(--navy);
  }
  .job {
    position: absolute; top: 75px; left: 22px; right: 21px;
  }
  .job-title {
    background: var(--band);
    height: 26px; line-height: 26px;
    text-align: center; font-weight: 700; font-size: 16px;
  }
  .job-summary {
    margin: 8px 2px 0; line-height: 18px; text-align: justify;
  }
  .job-award {
    margin-top: 6px; text-align: center;
    color: var(--navy); font-weight: 700; font-size: 14.5px;
  }
  .achievements { list-style: none; margin: 6px 2px 0 0; }
  .achievements li {
    position: relative; padding-left: 44px;
    line-height: 18.5px; margin-bottom: 6px; text-align: justify;
  }
  .achievements li::before {
    content: ""; position: absolute; left: 25px; top: 7px;
    width: 5px; height: 5px; background: var(--ink);
  }
  .achievements strong { font-weight: 700; }
  .education {
    position: absolute; top: 276px; left: 14px; width: 918px; height: 77px;
    border: 1px solid var(--frame);
    text-align: center; padding-top: 5px; line-height: 21px;
  }
  .education .training { margin-top: 5px; }
</style>
</head>
<body>
  <header class="page-header">
    <span class="candidate-name">Derek W. Folsom</span>
    <span class="page-number">Page | 3</span>
  </header>

  <section class="job">
    <h2 class="job-title">Indirect Account Executive (1999 – 2002)</h2>
    <p class="job-summary">Challenged with turning around underperforming accounts including Harlow’s, Brenton’s, DeskPoint, and WorkSupply. Managed 30 national and local third-party locations in Hampton Roads area.</p>
    <p class="job-award">Earned Vantel’s Pinnacle Club Award in 2001, one of only 10 out of 500 account executives in job category.</p>
    <ul class="achievements">
      <li><strong>Volt Mart Account:</strong> Assigned high-status Volt Mart account; achieved #1 national ranking in 2001 for productivity.</li>
      <li><strong>Best Practices:</strong> Selected to collaborate with national account manager to share best practices for use nationally and in the field; provided unparalleled support and assistance to store personnel in a highly competitive market</li>
      <li><strong>Norfolk Team:</strong> Made significant contributions to Norfolk team that became #1 indirect team in the country in 2001.</li>
    </ul>
  </section>

  <section class="education">
    <p>BACHELOR OF SCIENCE, Tidewater State University, Norfolk, VA</p>
    <p>National Collegiate Division I Four-Year Letterman in Baseball, Scholarship Student Athlete</p>
    <p class="training">COMPLETED NUMEROUS TRAINING SEMINARS in CloudTrack, selling skills, presentation skills, and executing profitable growth.</p>
  </section>
</body>
</html>
```